Diesel Fitting/Mechanical Company Needs a new Business Card

We would like a new business card that showcases our logo and business information.

Industry/Entity Type

Business

Contact Information for Business Card

314 Wendale Street
PO Box 7581 KELVALE QLD 4731
Phone: 49312787 Fax: 49312688 Mobile: 0438915276 ABN: 63 519 087 342

Requirements
Must have
• The following email addresses:
• admin@tkservicing.com.au , sales@tkservicing.com.au , accounts@tkservicing.com.au , parts@tkservicing.com.au , office@tkservicing.com.au
• Also need to have the website: www.tkservicing.com.au

```html
<!DOCTYPE html>
<html lang="en">
<head>
<meta charset="utf-8">
<title>TK Servicing – Business Card</title>
<link rel="stylesheet" href="https://fonts.googleapis.com/css2?family=Questrial&display=swap">
<style>
  :root {
    --page-bg: #e9e6e1;
    --card-dark: #111111;
    --card-dark-edge: #2a2a2a;
    --card-white: #ffffff;
    --rule-grey: #8c8c8c;
    --text-light: #e8e8e8;
    --accent-orange: #f07d22;
    --accent-yellow: #f2b21b;
  }
  * { box-sizing: border-box; margin: 0; padding: 0; }
  html, body {
    width: 1200px; height: 1024px; overflow: hidden;
    background: var(--page-bg);
    font-family: "Questrial", "Century Gothic", sans-serif;
  }
  .card {
    position: absolute;
    width: 760px; height: 434px;
    border-radius: 4px;
    overflow: hidden;
    box-shadow: 0 10px 28px rgba(0,0,0,.28);
    background: radial-gradient(ellipse at 35% 40%, var(--card-dark-edge) 0%, var(--card-dark) 70%);
  }
  .card-front { left: 60px; top: 50px; }
  .card-back { left: 380px; top: 540px; }

  .brand {
    display: flex; align-items: center; gap: 14px;
    color: var(--accent-orange);
    font-size: 38px; letter-spacing: 1px;
    white-space: nowrap;
  }
  .brand-dot {
    width: 26px; height: 26px; border-radius: 50%;
    background: var(--accent-orange);
  }
  .card-front .brand { position: absolute; left: 50px; top: 70px; }

  .contact {
    position: absolute; left: 50px; bottom: 52px;
    display: flex; gap: 26px;
    color: var(--text-light);
    font-size: 15px; line-height: 1.6;
    white-space: nowrap;
  }
  .contact-col { padding-left: 22px; border-left: 1px solid var(--accent-orange); }
  .contact-col:first-child { padding-left: 0; border-left: none; }
  .label { color: var(--accent-yellow); }
  .label.orange { color: var(--accent-orange); }

  .notes {
    position: absolute; left: 0; top: 0; bottom: 0; width: 430px;
    background: var(--card-white);
    padding: 60px 40px 0;
  }
  .notes-line { height: 1px; background: var(--rule-grey); margin-bottom: 72px; }
  .card-back .brand { position: absolute; right: 40px; top: 60px; font-size: 32px; }
</style>
</head>
<body>
  <section class="card card-front" aria-label="Business card front">
    <div class="brand"><span class="brand-dot"></span><span class="brand-name">TK Servicing</span></div>
    <div class="contact">
      <div class="contact-col">
        <div><span class="label">P:</span> 49312787</div>
        <div><span class="label">F:</span> 49312688</div>
        <div><span class="label">M:</span> 0438915276</div>
        <div><span class="label">ABN:</span> 63 519 087 342</div>
      </div>
      <div class="contact-col">
        <div><span class="label orange">E:</span> admin@tkservicing.com.au</div>
        <div><span class="label orange">E:</span> sales@tkservicing.com.au</div>
        <div><span class="label orange">E:</span> accounts@tkservicing.com.au</div>
        <div><span class="label orange">E:</span> parts@tkservicing.com.au</div>
        <div><span class="label orange">E:</span> office@tkservicing.com.au</div>
      </div>
      <div class="contact-col">
        <div><span class="label orange">A:</span> 314 Wendale Street</div>
        <div>PO Box 7581</div>
        <div>KELVALE QLD 4731</div>
        <div><span class="label orange">W:</span> www.tkservicing.com.au</div>
      </div>
    </div>
  </section>

  <section class="card card-back" aria-label="Business card back">
    <div class="notes">
      <div class="notes-line"></div>
      <div class="notes-line"></div>
      <div class="notes-line"></div>
      <div class="notes-line"></div>
    </div>
    <div class="brand"><span class="brand-dot"></span><span class="brand-name">TK Servicing</span></div>
  </section>
</body>
</html>
```